Large online photo magazine needs redesign

We have previously digitised a historical photographic magazine of around 20,000 printed pages and made it available online. The magazine ran up to the early 1970s, and the content is largely black and white photographs of local events, accompanied by short captions.

Although the content is very rich, the design needs to be revisited so that:
* it is visually appealing
* it is responsive (i.e. works in browsers across all manner of devices)
* is faithful to the nature of the content

There are only a few core page types, and the central one is the article page, an example of which can be seen at:
http://tawaleaf.org.nz/gisborne/issue/KMW73_19600714/t1-body-d4.html

Any design submitted should be based on the treatment of an article page such as the above.

Given the large number of pages on our site, we need a design which can be templated to work for any content in the collection, i.e. we cannot hand-craft our templates to match a given page of content, rather a template must work acceptably well for all content.

The current site, although basic in design, has the advantage that it is quite efficient in the amount of data per page request (around 100k - 200k). While not adverse to web fonts, banner imagery etc, we will carefully consider the benefit gained from any such treatment against the amount of extra data that needs to be downloaded to the client's browser.

For the right design, we are able ourselves to adapt it to a CSS layout.

An example of each core page type is as follows (though for this project we only expect a design for a single page, as itemised above):

http://tawaleaf.org.nz/gisborne/index.html
http://tawaleaf.org.nz/gisborne/about.html
http://tawaleaf.org.nz/gisborne/help.html
http://tawaleaf.org.nz/gisborne/initial/index.html
http://tawaleaf.org.nz/gisborne/search/results?type=section&text=smith&cmdSubmit=Go
http://tawaleaf.org.nz/gisborne/advanced-search/index.html
http://tawaleaf.org.nz/gisborne/issue/KMW73_19600714/t1-front-d1.html
http://tawaleaf.org.nz/gisborne/issue/KMW73_19600714/index.html
http://tawaleaf.org.nz/gisborne/issue/KMW73_19600714/fig-KMW73_19600714_005a.html
http://tawaleaf.org.nz/gisborne/issue/KMW73_19600714/KMW73_19600714_012.html
http://tawaleaf.org.nz/gisborne/issue/KMW73_19600714/thumbnails.html

Reason: Extending the deadline by three days as a number of designers have only recently accepted the invitation.

A general browsing audience of all ages, but skewed towards the older generations, and those interested in family / regional history.

The average user will not be particularly web-savy, and the treatment of the content should not detract / distract from the actual content itself.

Events

• * it is visually appealing
The content should be visually appealing to the audience, which can be defined as a general browsing audience of all ages, but skewed towards the middle and older generations.

* it is responsive (the design can be adapted - by us - to work in browsers across all manner of devices)

The magazine covers (http://tawaleaf.org.nz/gisborne/issues/index.html) offer some possible inspiration for treatment of the material.

```html
<!DOCTYPE html>
<html lang="en">
<head>
<meta charset="utf-8">
<title>Tawa Leaf Pictorial</title>
<link rel="stylesheet" href="https://fonts.googleapis.com/css2?family=Source+Sans+3:ital,wght@0,400;0,500;0,600;0,700;1,400;1,600&display=swap">
<style>
:root{
  --brand:#c93b51;
  --brand-dark:#b52f44;
  --nav-top:#454545;
  --nav-bottom:#232323;
  --panel:#efefef;
  --rule:#dcdcdc;
  --ink:#444;
  --muted:#7a7a7a;
  --footer:#3b3b3b;
  --white:#fff;
}
*{box-sizing:border-box;margin:0;padding:0}
html,body{width:1200px;height:1194px;overflow:hidden}
body{font-family:"Source Sans 3",Arial,sans-serif;color:var(--ink);background:var(--white);position:relative}
a{color:inherit;text-decoration:none}

.site-header{height:107px;background:var(--brand);position:relative}
.brand{position:absolute;left:134px;top:34px;display:flex;align-items:center;gap:12px;color:var(--white);font-size:36px;font-weight:700;letter-spacing:.5px}
.brand-mark{width:26px;height:26px;background:var(--white);border-radius:50%}
.utility{position:absolute;right:133px;top:18px;display:flex;font-size:14px;color:var(--white)}
.utility a{padding:0 14px;border-left:1px solid rgba(255,255,255,.7)}
.utility a:first-child{border:none;padding-left:0}
.utility a:last-child{padding-right:0}
.search{position:absolute;left:828px;top:59px;display:flex}
.search input{width:207px;height:31px;border:none;padding:0 13px;font:italic 12px "Source Sans 3",sans-serif;color:#999;outline:none}
.search button{width:33px;height:31px;border:none;background:#222;display:flex;align-items:center;justify-content:center}

.main-nav{height:46px;background:linear-gradient(var(--nav-top),var(--nav-bottom));display:flex;padding-left:130px}
.main-nav a{color:var(--white);font-size:14px;line-height:48px;text-align:center;border-right:1px solid #1a1a1a;box-shadow:1px 0 0 #555}
.main-nav .nav-home{width:70px;text-align:left;padding-left:8px}
.main-nav .nav-about{width:99px}
.main-nav .nav-browse{width:240px}
.main-nav .nav-az{width:122px;border:none;box-shadow:none}

.sidebar{position:absolute;left:130px;top:179px;width:220px}
.box-head{height:41px;background:var(--brand);color:var(--white);font-size:19px;font-weight:600;padding:12px 16px 0}
.links{background:var(--panel);padding:14px 0 12px}
.links li{list-style:none;height:30.6px;border-bottom:1px solid var(--rule);padding-left:16px;font-size:14px;color:#555;display:flex;align-items:center;gap:9px}
.links li:last-child{border:none}
.email-box{margin-top:25px;background:var(--brand);height:184px}
.email-box .box-head{height:40px;border-bottom:1px solid var(--brand-dark);padding-left:15px}
.email-box p{color:var(--white);font-size:12.5px;line-height:17px;padding:12px 16px 0}
.email-box input{display:block;margin:10px 0 0 15px;width:191px;height:33px;border:none;padding:0 12px;font:italic 12px "Source Sans 3",sans-serif;color:#aaa}
.email-box button{display:block;margin:12px 0 0 114px;width:91px;height:31px;background:linear-gradient(#3d3d3d,#1f1f1f);color:var(--white);border:1px solid #111;font:500 12px "Source Sans 3",sans-serif}
.editor{margin-top:26px}
.editor .box-head{background:#2b2b2b;font-weight:400;padding-left:18px}
.editor-item{background:var(--panel);padding:18px 15px 16px;border-bottom:1px solid var(--rule)}
.editor-item:last-child{border:none;padding-top:14px;padding-bottom:20px}
.editor-item h4{font-size:14px;font-weight:500;color:#555;margin-bottom:8px}
.editor-item p{font-size:14px;line-height:17px;color:#888}
.more{display:block;margin-top:5px;font-style:italic;font-size:13px;color:var(--brand)}

.stories{position:absolute;left:370px;top:179px;width:700px}
.story{height:197px;background:var(--panel);margin-bottom:20px;position:relative}
.story:nth-child(2){margin-bottom:21px}
.story:nth-child(3){margin-bottom:22px}
.photo{position:absolute;left:18px;top:20px;width:203px;height:155px;border:3px solid var(--white);box-shadow:0 0 2px rgba(0,0,0,.3)}
.story h2{position:absolute;left:241px;top:14px;font-size:25px;font-weight:400;color:var(--brand)}
.story .body{position:absolute;left:243px;top:61px;width:440px;font-size:13.5px;line-height:18px;color:var(--muted);white-space:nowrap}
.story .body p+p{margin-top:20px}
.read{font-style:italic;font-weight:600;font-size:12px;color:var(--brand);margin-left:4px}

.pager{position:absolute;left:838px;top:1048px;display:flex;align-items:center;gap:4px;font-size:10px;color:#999}
.pager .label{margin-right:12px}
.pager a{width:20px;height:19px;background:#e2e2e2;text-align:center;line-height:19px;color:#777}
.pager a.current{background:#888;color:var(--white)}
.pager .next{margin-left:10px}

.site-footer{position:absolute;left:0;top:1098px;width:1200px;height:96px;background:var(--footer)}
.site-footer small{position:absolute;left:133px;top:38px;font-size:14px;color:#ccc}
.social{position:absolute;left:907px;top:1131px;display:flex;gap:3px}
.social span{width:29px;height:29px;border-radius:50%;background:#bbb;display:flex;align-items:center;justify-content:center}
</style>
</head>
<body>
<header class="site-header">
  <a class="brand" href="http://tawaleaf.org.nz/archive/index.html"><span class="brand-mark"></span>Tawa Leaf Pictorial</a>
  <nav class="utility">
    <a href="http://tawaleaf.org.nz/archive/advanced-search/index.html">Advanced search</a>
    <a href="http://tawaleaf.org.nz/archive/help.html">Help</a>
    <a href="#">Report an error</a>
  </nav>
  <form class="search">
    <input type="text" placeholder="Search Tawa Leaf Pictorial..">
    <button type="button" aria-label="Search"><svg width="18" height="18" viewBox="0 0 18 18"><circle cx="7" cy="7" r="5" fill="none" stroke="#fff" stroke-width="2"/><line x1="10.5" y1="10.5" x2="16" y2="16" stroke="#fff" stroke-width="3"/></svg></button>
  </form>
</header>
<nav class="main-nav">
  <a class="nav-home" href="http://tawaleaf.org.nz/archive/index.html">Home</a>
  <a class="nav-about" href="http://tawaleaf.org.nz/archive/about.html">About</a>
  <a class="nav-browse" href="http://tawaleaf.org.nz/archive/issues/index.html">Browse Tawa Leaf Pictorial</a>
  <a class="nav-az" href="http://tawaleaf.org.nz/archive/people/index.html">A-Z people</a>
</nav>

<aside class="sidebar">
  <section>
    <h3 class="box-head">Useful Links</h3>
    <ul class="links">
      <li><svg width="9" height="8" viewBox="0 0 9 8"><path d="M0 4h7M4 1l3 3-3 3" stroke="#444" fill="none" stroke-width="1.3"/></svg>Sed ut perspiciatis unde</li>
      <li><svg width="9" height="8" viewBox="0 0 9 8"><path d="M0 4h7M4 1l3 3-3 3" stroke="#444" fill="none" stroke-width="1.3"/></svg>omni natus error sit</li>
      <li><svg width="9" height="8" viewBox="0 0 9 8"><path d="M0 4h7M4 1l3 3-3 3" stroke="#444" fill="none" stroke-width="1.3"/></svg>voluptatem accusantium</li>
      <li><svg width="9" height="8" viewBox="0 0 9 8"><path d="M0 4h7M4 1l3 3-3 3" stroke="#444" fill="none" stroke-width="1.3"/></svg>doloremque laudantium</li>
      <li><svg width="9" height="8" viewBox="0 0 9 8"><path d="M0 4h7M4 1l3 3-3 3" stroke="#444" fill="none" stroke-width="1.3"/></svg>totam rem aperiam</li>
      <li><svg width="9" height="8" viewBox="0 0 9 8"><path d="M0 4h7M4 1l3 3-3 3" stroke="#444" fill="none" stroke-width="1.3"/></svg>ipsa quae ab illo inventore</li>
      <li><svg width="9" height="8" viewBox="0 0 9 8"><path d="M0 4h7M4 1l3 3-3 3" stroke="#444" fill="none" stroke-width="1.3"/></svg>veritatis et quasi architecto</li>
      <li><svg width="9" height="8" viewBox="0 0 9 8"><path d="M0 4h7M4 1l3 3-3 3" stroke="#444" fill="none" stroke-width="1.3"/></svg>beatae vitae dicta sunt</li>
    </ul>
  </section>
  <section class="email-box">
    <h3 class="box-head">Get Email News</h3>
    <p>Duis aute irure dolor in reprehener nderit in voluptate velit.</p>
    <input type="email" placeholder="Enter your Email...">
    <button type="button">SUBMIT</button>
  </section>
  <section class="editor">
    <h3 class="box-head">Editor’s Pic</h3>
    <div class="editor-item">
      <h4>Excepteur sint occaecat cupida</h4>
      <p>Duis aute irure dolor in reprehen derit in voluptate velit.</p>
      <a class="more" href="#">view more &gt;&gt;</a>
    </div>
    <div class="editor-item">
      <h4>Excepteur sint occaecat cupida</h4>
      <p>Duis aute irure dolor in reprehen derit in voluptate velit.</p>
      <a class="more" href="#">view more &gt;&gt;</a>
    </div>
  </section>
</aside>

<main class="stories">
  <article class="story">
    <div class="photo" role="img" aria-label="Black and white photograph of three sisters in air hostess uniforms" style="background:linear-gradient(135deg,#9a9a9a,#3c3c3c)"></div>
    <h2>Flying Sisters from Awaroa</h2>
    <div class="body">
      <p>This is probably something of a record--three sisters who are all air host-<br>esses. They are the Harland sisters.....Marguerite, Ngaire, and Rosalind,<br>daughters of Mr and Mrs R. T. Harland, Ferncliff Road, Awaroa.</p>
      <p>She was the first air hostess to make a scheduled flight to Awaroa, on<br>Sunday of last week. <a class="read" href="http://tawaleaf.org.nz/archive/issue/TLP-041/story-4.html">Read More &gt;&gt;</a></p>
    </div>
  </article>
  <article class="story">
    <div class="photo" role="img" aria-label="Sepia photograph of a steel bridge across a river with a newspaper caption" style="background:linear-gradient(#d8d4c4,#77735f)"></div>
    <h2>Bridge in Splits</h2>
    <div class="body">
      <p>This is probably something of a record--three sisters who are all air host-<br>esses. They are the Harland sisters.....Marguerite, Ngaire, and Rosalind,<br>daughters of Mr and Mrs R. T. Harland, Ferncliff Road, Awaroa.</p>
      <p>She was the first air hostess to make a scheduled flight to Awaroa, on<br>Sunday of last week. <a class="read" href="#">Read More &gt;&gt;</a></p>
    </div>
  </article>
  <article class="story">
    <div class="photo" role="img" aria-label="Sepia portrait of an engaged couple" style="background:linear-gradient(135deg,#a89e86,#3a352b)"></div>
    <h2>Engaged</h2>
    <div class="body">
      <p>This is probably something of a record--three sisters who are all air host-<br>esses. They are the Harland sisters.....Marguerite, Ngaire, and Rosalind,<br>daughters of Mr and Mrs R. T. Harland, Ferncliff Road, Awaroa.</p>
      <p>She was the first air hostess to make a scheduled flight to Awaroa, on<br>Sunday of last week. <a class="read" href="#">Read More &gt;&gt;</a></p>
    </div>
  </article>
  <article class="story">
    <div class="photo" role="img" aria-label="Black and white portrait of a young man in a suit" style="background:linear-gradient(135deg,#8e8b82,#2a2926)"></div>
    <h2>Roving Camera</h2>
    <div class="body">
      <p>This is probably something of a record--three sisters who are all air host-<br>esses. They are the Harland sisters.....Marguerite, Ngaire, and Rosalind,<br>daughters of Mr and Mrs R. T. Harland, Ferncliff Road, Awaroa.</p>
      <p>She was the first air hostess to make a scheduled flight to Awaroa, on<br>Sunday of last week. <a class="read" href="#">Read More &gt;&gt;</a></p>
    </div>
  </article>
</main>

<nav class="pager">
  <span class="label">Page 1 of 32</span>
  <a class="current" href="#">1</a><a href="#">2</a><a href="#">3</a><a href="#">4</a><a href="#">5</a><a href="#">6</a>
  <svg class="next" width="10" height="12" viewBox="0 0 10 12"><path d="M2 1l5 5-5 5" stroke="#888" stroke-width="2.5" fill="none"/></svg>
</nav>

<footer class="site-footer">
  <small>© 2014 Kowhai Street Memorial Library. All Right Reserved</small>
</footer>
<div class="social">
  <span aria-label="Email"><svg width="17" height="12" viewBox="0 0 17 12"><rect x="1" y="1" width="15" height="10" fill="none" stroke="#fff" stroke-width="1.5"/><path d="M1 1l7.5 6L16 1" fill="none" stroke="#fff" stroke-width="1.5"/></svg></span>
  <span aria-label="Social link"></span>
  <span aria-label="Social link"></span>
  <span aria-label="Social link"></span>
  <span aria-label="Social link"></span>
</div>
</body>
</html>
```